Book Cover for: TITLE Mend the Quiet Tide SUBTITLE For couples who don't want to break up

We need a full cover design for a book on relationships written by husband and wife team, Marla and Dennis Holtwick, PhD. This book will offer hope for couples that are on the verge of breaking up but want to work things out and stay together. The theme is to teach couples about their own reactions to their partner, how moods affect a relationship, how to get creative to solving problems and how to have a good feeling towards your partner regardless of differences. This book is about hope. It is a positive look at relationships that feel hopeless.

Target Market(s)

Married or couples that are going through a difficult time and are considering splitting up due to, communication difficulties, addiction, affair. We imagine the book will appeal to women more than men but still want a cover that men would be comfortable picking up.

Colors

Designer to choose colors to be used in the design.

Requirements
Must have
• We want the cover to beautiful, intriguing, simple and uncomplicated. We don't want it overly busy, technical, or complex.
Nice to have
• MAYBE?? a broken heart being put back together.
Should not have
• No photo, no cartoon, no flowers, no couple (unless obscure and not gender specific).

```html
<!DOCTYPE html>
<html lang="en">
<head>
<meta charset="utf-8">
<title>Mend the Quiet Tide – Full Cover</title>
<link href="https://fonts.googleapis.com/css2?family=Montserrat:wght@500;600;700&display=swap" rel="stylesheet">
<style>
  :root {
    --flap: #2f2a6c;
    --back-top: #4b2f9c;
    --back-bottom: #3a2a86;
    --spine: #3a2f86;
    --front-top: #b34fb8;
    --front-mid: #6d2fa8;
    --front-bottom: #2a1f66;
    --white: #ffffff;
    --pink: #f09ad8;
    --sky: #38b8ea;
  }
  * { margin: 0; padding: 0; box-sizing: border-box; }
  html, body { width: 1200px; height: 842px; overflow: hidden; background: #1d1848; }
  body { font-family: "Montserrat", Arial, sans-serif; }
  .cover { position: relative; width: 1200px; height: 842px; overflow: hidden; }

  .flap { position: absolute; left: 0; top: 0; width: 195px; height: 842px; background: var(--flap); }
  .back { position: absolute; left: 195px; top: 0; width: 358px; height: 842px;
          background: linear-gradient(180deg, var(--back-top), var(--back-bottom)); }
  .spine { position: absolute; left: 553px; top: 0; width: 94px; height: 842px; background: var(--spine); }
  .front { position: absolute; left: 647px; top: 0; width: 553px; height: 842px;
           background: radial-gradient(ellipse at 70% 0%, var(--front-top) 0%, var(--front-mid) 45%, var(--front-bottom) 100%); }

  .flap-title { position: absolute; left: 33px; top: 46px; color: var(--white);
                font-weight: 700; font-size: 28px; line-height: 26px; letter-spacing: -0.5px; }
  .flap-subtitle { position: absolute; left: 33px; top: 129px; color: var(--sky);
                   font-weight: 600; font-size: 8.6px; line-height: 11px; text-transform: uppercase; }
  .flap-bio { position: absolute; left: 32px; top: 172px; width: 154px; color: var(--pink);
              font-weight: 600; font-size: 8.6px; line-height: 16px; }

  .back-copy { position: absolute; left: 13px; top: 42px; width: 302px; }
  .back-lead { color: var(--pink); font-weight: 600; font-size: 13px; line-height: 21.3px; text-align: justify; }
  .back-body { color: var(--white); font-weight: 600; font-size: 10.2px; line-height: 21.5px; text-align: justify; }

  .spine-title, .spine-author { position: absolute; left: 47px; transform-origin: 0 0;
                                transform: rotate(90deg); white-space: nowrap; }
  .spine-title { top: 36px; color: var(--white); font-weight: 700; font-size: 29px; letter-spacing: 0.5px; margin-left: 15px; }
  .spine-author { top: 495px; color: var(--pink); font-weight: 700; font-size: 15.5px; margin-left: 9px; }

  .front-title { position: absolute; left: 0; top: 54px; width: 553px; text-align: center;
                 color: var(--white); font-weight: 700; font-size: 94px; line-height: 88px; letter-spacing: -2px; }
  .front-subtitle { position: absolute; left: 0; top: 326px; width: 553px; text-align: center;
                    color: var(--sky); font-weight: 700; font-size: 18.5px; }
  .front-art { position: absolute; left: 137px; top: 368px; width: 296px; height: 296px; }
  .front-author { position: absolute; left: 0; top: 736px; width: 553px; text-align: center;
                  color: var(--pink); font-weight: 700; font-size: 24px; }
</style>
</head>
<body>
<div class="cover">
  <section class="flap">
    <h2 class="flap-title">MEND THE<br>QUIET<br>TIDE</h2>
    <p class="flap-subtitle">For couples<br>who don't want to break up</p>
    <p class="flap-bio">Marla and Dennis Holtwick Ph.D. have been working with couples for several decades with an incredible success rate. They are co-partners at Tidewell and Associates, an educational organization in the Pacific Northwest, which provides consulting services for individuals, couples, parents, as well as leadership training for businesses and organizations. They have the same objective for everyone they work with; to help people have more hope and fulfillment in their lives, as well as function more synergistically. The diversity of Tidewell and Associates clientele is attributed to their unique understanding of human functioning and interaction, the application of which has significant impact on interpersonal relationships.<br>They have curated a selection of recordings and books over the years to restore the good feeling between you and your partner. Their previous book, The Steady Harbor Handbook, is packed full of wisdom and practical perspective shifts that has the potential to change any relationship. Learn more at www.tidewellassociates.com.</p>
  </section>

  <section class="back">
    <div class="back-copy">
      <p class="back-lead">Have you ever wondered how you can go from being so deeply in love with your partner to finding yourself miserable in your relationship? What happened? This book sheds light on that question and the human dilemma around relationships.</p>
      <p class="back-body">Marla and Dennis Holtwick Ph.D. have been married for forty-five years and found their way out of their own troubled relationship. In this book, they propose a new approach that helps you live more gracefully with your partner's flaws which allows you to put issues to rest, resolve differences, and move forward in your relationship with renewed love and commitment.</p>
      <p class="back-body">Broken up into an easy, digestible format that includes real client vignettes and success stories, this book is essential for the struggling couple and has the potential to lead to a fresh start even when you have lost all hope.</p>
    </div>
  </section>

  <section class="spine">
    <h2 class="spine-title">MEND THE QUIET TIDE</h2>
    <p class="spine-author">MARLA AND DENNIS HOLTWICK,PhD</p>
  </section>

  <section class="front">
    <h1 class="front-title">MEND THE<br>QUIET<br>TIDE</h1>
    <p class="front-subtitle">FOR COUPLES WHO DON'T WANT TO BREAK UP</p>
    <svg class="front-art" viewBox="0 0 296 296" role="img" aria-label="Cracked stone heart held inside a glowing glass sphere">
      <defs>
        <radialGradient id="orb" cx="50%" cy="45%" r="55%">
          <stop offset="0%" stop-color="#c76fd4"/>
          <stop offset="55%" stop-color="#8a44b8"/>
          <stop offset="100%" stop-color="#6a4bbf" stop-opacity="0.55"/>
        </radialGradient>
      </defs>
      <circle cx="148" cy="148" r="146" fill="url(#orb)"/>
    </svg>
    <p class="front-author">MARLA AND DENNIS HOLTWICK,PhD</p>
  </section>
</div>
</body>
</html>
```